Lumen! Consulting

We need a web design for a new supply chain consulting business. we will work with major brands in the electronics, apparel, toy and jewelry industries to create a sustainability program for our customers and implement in their supply chain. We want our customers to have confidence in their supply chain responsibility program. We also manage stakeholder engagements, NGO relationships, and external communications.

I would like to colors to be green, orange and/or black to match the logo (attached). The final design should communicate positive and optimistic leadership - for a professional, sustainable, business.

Industry/Entity Type

Business

```html
<!DOCTYPE html>
<html lang="en">
<head>
<meta charset="utf-8">
<title>Lumen! Consulting</title>
<link href="https://fonts.googleapis.com/css2?family=Open+Sans:ital,wght@0,400;0,600;1,400&display=swap" rel="stylesheet">
<style>
:root{
  --orange:#f39c1f;
  --green:#7cc242;
  --ink:#4a4a4a;
  --text:#666;
  --muted:#999;
  --line:#e6e6e6;
  --band:#f4f4f4;
  --footer:#1f1f1f;
  --white:#fff;
}
*{margin:0;padding:0;box-sizing:border-box}
html,body{width:840px;height:1200px;overflow:hidden}
body{position:relative;background:var(--white);font-family:"Open Sans",Arial,sans-serif;color:var(--text)}
.abs{position:absolute}
/* header */
.site-header{position:absolute;left:0;top:0;width:840px;height:66px;background:var(--white)}
.brand{position:absolute;left:62px;top:22px;display:flex;align-items:center;gap:6px;color:var(--orange);font-size:17px;font-weight:400}
.brand-dot{width:12px;height:12px;border-radius:50%;background:var(--green)}
.main-nav{position:absolute;top:0;left:263px;height:66px;font-size:10px;color:#555}
.main-nav a{position:absolute;top:0;height:66px;line-height:66px;text-decoration:none;color:inherit;white-space:nowrap;transform:translateX(-50%)}
.main-nav a.active{background:var(--orange);color:var(--white);width:62px;text-align:center;transform:none;left:0}
/* hero */
.hero{position:absolute;left:0;top:66px;width:840px;height:398px;background:linear-gradient(100deg,#9fb3c4 0%,#d9dde0 30%,#c7c2bb 55%,#8f959a 80%,#cfd8e0 100%)}
.hero-title{position:absolute;left:65px;top:242px;font-size:30px;font-weight:600;line-height:39px;color:#4b4e52}
.slider-dots{position:absolute;left:296px;top:361px;width:250px;height:10px}
.slider-dots .rule{position:absolute;top:4px;height:1px;background:#b9b9b9}
.slider-dots i{position:absolute;top:1px;width:7px;height:7px;border-radius:50%;background:#222}
.slider-dots i.on{background:var(--green);border:1.5px solid #fff}
/* brands */
.section-title{font-size:16px;font-weight:600;color:var(--ink)}
.brand-card{position:absolute;top:524px;width:224px;height:148px;border:1px solid #ddd;padding:2px;background:#fff;box-shadow:0 6px 6px -5px rgba(0,0,0,.3)}
.brand-card .photo{width:100%;height:100%}
.brand-card .label{position:absolute;left:3px;top:84px;height:25px;line-height:25px;padding:0 12px;background:var(--orange);color:#fff;font-size:12px;font-weight:600}
.brand-card .more{position:absolute;left:3px;top:112px;height:22px;line-height:22px;padding:0 7px;background:var(--green);color:#fff;font-size:7.5px}
.arrow{position:absolute;top:587px;width:22px;height:22px}
.divider{position:absolute;left:0;top:710px;width:840px;height:1px;background:var(--line)}
/* about */
.video{position:absolute;left:65px;top:783px;width:161px;height:133px;border:1px solid #ddd;padding:2px;background:#fff}
.video .photo{width:100%;height:100%;background:linear-gradient(90deg,#f4f4f4 45%,#c9a88e 80%,#eee 100%)}
.play{position:absolute;left:66px;top:52px;width:28px;height:28px;border-radius:50%;background:rgba(60,60,60,.75)}
.lead{position:absolute;left:246px;top:793px;width:250px;font-size:10.5px;line-height:16px;font-weight:600;color:var(--orange)}
.body-copy{position:absolute;left:246px;top:836px;width:262px;font-size:8px;line-height:15.5px;color:var(--text)}
/* news */
.news-item{position:absolute;left:530px;width:250px}
.date{position:absolute;left:0;top:0;width:45px;height:54px;background:var(--green);color:#fff;text-align:center}
.date b{display:block;height:31px;line-height:33px;font-size:17px;font-weight:600;color:#3d5a1f;border-bottom:1px solid rgba(255,255,255,.7)}
.date span{display:block;line-height:22px;font-size:12px}
.news-item h3{position:absolute;left:62px;top:1px;font-size:10.5px;font-weight:600;color:var(--orange);white-space:nowrap}
.news-item p{position:absolute;left:62px;top:20px;width:190px;font-size:8px;line-height:12px;color:var(--text)}
.news-item em{position:absolute;left:62px;top:46px;font-size:7.5px;color:var(--green)}
/* testimonials */
.band{position:absolute;left:0;top:954px;width:840px;height:176px;background:var(--band);border-top:1px solid var(--line)}
.quote{position:absolute;top:988px;width:210px;height:62px;background:#fff;border:1px solid #e3e3e3;padding:9px 9px;font-size:8.5px;line-height:14.5px;font-style:italic;color:var(--muted)}
.quote::after{content:"";position:absolute;left:26px;bottom:-8px;border:8px solid transparent;border-top-color:#fff;border-bottom:0;border-left-width:0}
.avatar{position:absolute;top:1064px;width:44px;height:44px;border-radius:50%;background:linear-gradient(#8a8d90,#5d6064)}
.person{position:absolute;top:1072px;font-size:9px;line-height:14.5px;color:var(--orange)}
.person span{display:block;color:var(--green)}
/* footer */
.site-footer{position:absolute;left:0;top:1130px;width:840px;height:70px;background:var(--footer)}
.social{position:absolute;left:65px;top:25px;display:flex;gap:6.4px}
.social i{width:20px;height:20px;border-radius:50%;background:#4b4b4b}
.social i.on{background:var(--green)}
.footer-links{position:absolute;right:62px;top:29px;font-size:8.5px;color:#ddd;white-space:nowrap}
</style>
</head>
<body>
<header class="site-header">
  <div class="brand"><span class="brand-dot"></span>Lumen!</div>
  <nav class="main-nav">
    <a class="active" href="#">Home</a>
    <a href="#" style="left:103px">About us</a>
    <a href="#" style="left:179px">Services</a>
    <a href="#" style="left:251px">Gallery</a>
    <a href="#" style="left:319px">Blog</a>
    <a href="#" style="left:395px">Testimonials</a>
    <a href="#" style="left:489px">Contact us</a>
  </nav>
</header>

<section class="hero" role="img" aria-label="Consultant reviewing documents with two smiling clients">
  <h1 class="hero-title">New Supply Chain<br>Consulting Business</h1>
  <div class="slider-dots">
    <span class="rule" style="left:0;width:94px"></span>
    <i style="left:103px"></i><i class="on" style="left:115px"></i><i style="left:127px"></i><i style="left:138px"></i>
    <span class="rule" style="left:154px;width:96px"></span>
  </div>
</section>

<h2 class="section-title abs" style="left:0;width:840px;top:484px;text-align:center">Works And Major Brands</h2>
<svg class="arrow" style="left:31px" viewBox="0 0 22 22"><circle cx="11" cy="11" r="10" fill="#fff" stroke="#aaa" stroke-width="1.2"/><path d="M13 6 L8 11 L13 16" fill="none" stroke="#999" stroke-width="2"/></svg>
<svg class="arrow" style="left:786px" viewBox="0 0 22 22"><circle cx="11" cy="11" r="10" fill="#fff" stroke="#aaa" stroke-width="1.2"/><path d="M9 6 L14 11 L9 16" fill="none" stroke="#999" stroke-width="2"/></svg>
<article class="brand-card" style="left:65px">
  <div class="photo" role="img" aria-label="Laptop and phone on a desk" style="background:linear-gradient(135deg,#e9eef0,#c7ced3 60%,#f2f2f2)"></div>
  <span class="label">Electronics</span><span class="more">Read More</span>
</article>
<article class="brand-card" style="left:308px">
  <div class="photo" role="img" aria-label="Clothing on mannequins in a store" style="background:linear-gradient(90deg,#6b5a48,#2a2a2a 40%,#b59a3a 70%,#3a3430)"></div>
  <span class="label">Apparel</span><span class="more">Read More</span>
</article>
<article class="brand-card" style="left:550px">
  <div class="photo" role="img" aria-label="Couple browsing a jewellery display" style="background:linear-gradient(90deg,#c79a6a,#5f8fb0 50%,#8fd0ea)"></div>
  <span class="label">Jewellery</span><span class="more">Read More</span>
</article>

<div class="divider"></div>

<h2 class="section-title abs" style="left:65px;top:735px">What is Supply Chain Consulting</h2>
<div class="video">
  <div class="photo" role="img" aria-label="Man drawing a supply chain cycle diagram"></div>
  <svg class="play" viewBox="0 0 28 28"><path d="M11 8 L20 14 L11 20 Z" fill="#fff"/></svg>
</div>
<p class="lead">Lorem ipsum dolor sit amet, consectetuer adipi-scing elit. Praesent vestibulum</p>
<p class="body-copy">Lorem ipsum dolor sit amet, consectetuer adipiscing elit. Praesent vestibulum molestie lacuAenean nonummy hendreritlore mauris. Phasellus porta. Fusce suscipit varius mi. Lorem ipsum dolor sit amet, consectetuer adipiscing elit.</p>

<h2 class="section-title abs" style="left:530px;top:735px">News &amp; Events</h2>
<article class="news-item" style="top:783px">
  <div class="date"><b>23</b><span>oct</span></div>
  <h3>Lorem ipsum dolor sit amet, con.</h3>
  <p>Praesent vestibulum molestie lacuAenean nonummy hendrerit mauris. Phasellus porta.</p>
  <em>Fusce suscipit varius</em>
</article>
<article class="news-item" style="top:862px">
  <div class="date"><b>23</b><span>oct</span></div>
  <h3>Lorem ipsum dolor sit amet, con.</h3>
  <p>Praesent vestibulum molestie lacuAenean nonummy hendrerit mauris. Phasellus porta.</p>
  <em>Fusce suscipit varius</em>
</article>

<section class="band"></section>
<blockquote class="quote" style="left:65px">Lorem ipsum dolor sit amet, consectetur adipi-sicing elit. Aliquid consequuntur unde quae totam recusandae</blockquote>
<blockquote class="quote" style="left:315px">Lorem ipsum dolor sit amet, consectetur adipi-sicing elit. Aliquid consequuntur unde quae totam recusandae</blockquote>
<blockquote class="quote" style="left:565px">Lorem ipsum dolor sit amet, consectetur adipi-sicing elit. Aliquid consequuntur unde quae totam recusandae</blockquote>
<div class="avatar" style="left:65px" role="img" aria-label="Client portrait"></div>
<div class="avatar" style="left:315px" role="img" aria-label="Client portrait"></div>
<div class="avatar" style="left:565px" role="img" aria-label="Client portrait"></div>
<p class="person" style="left:120px">Marian Holt<span>CEO loremip</span></p>
<p class="person" style="left:370px">Marian Holt<span>CEO loremip</span></p>
<p class="person" style="left:620px">Marian Holt<span>CEO loremip</span></p>

<footer class="site-footer">
  <div class="social"><i></i><i class="on"></i><i></i><i></i><i></i><i></i><i></i></div>
  <p class="footer-links">Home | About | Services | Estimate | Contact Us | Copyright Lumen 2014. All Rights Reserved.</p>
</footer>
</body>
</html>
```